New Lead input page design

Attached is our concept of a new lead input screen for the back-end of our website which is a tool for a loan agent (2 page PDF attached)

1. This is the first of many other data input screen projects for our website, so the designer that ends up with us will have quite a bit of add on new projects.

2. HERE IS THE LINK WITH THE SAMPLE OF ALL THE CURRENT CONTROLS:
http://apps.brimtally.com/controlWidgets.html

3. The colors and hues of: either GREEN & GREYS or BLUE & GREYS.

4. I think some gradients and shadows adds depth and sophistication. Basically trying to get away from old school flat, one dimensional data screen inputs and add some design flare to it.

5. Upon completion we will need the HTML of the design etc and we will code the input fields directly.

6. See attached files for the entire input screen. Please also add the data input space (see sample) to your design.

Thank you

Reason: We are extending the deadline to give us time to ask current designs to complete slight revisions

Reason: Finalizing the selection for one last variation detailed to current designers

```html
<!DOCTYPE html>
<html lang="en">
<head>
<meta charset="utf-8">
<title>New Lead</title>
<link rel="stylesheet" href="https://fonts.googleapis.com/css2?family=Open+Sans:wght@400;700&display=swap">
<style>
:root{
  --page:#ffffff;
  --panel:#f5f5f5;
  --panel-edge:#e4e4e4;
  --nav-top:#a8c6f7;
  --nav-bottom:#8fb3f2;
  --nav-rule:#6d8fcf;
  --orb-light:#dbe8fd;
  --orb-dark:#8ab3f6;
  --label:#333333;
  --value:#555555;
  --footer:#ececec;
}
*{box-sizing:border-box;margin:0;padding:0}
html,body{width:837px;height:1200px;overflow:hidden;background:var(--page)}
body{position:relative;font-family:"Open Sans",Arial,sans-serif;font-size:9.6px;color:var(--value)}
.topnav{position:absolute;left:109px;top:25px;width:619px;height:48px;
  background:linear-gradient(var(--nav-top),var(--nav-bottom));
  border-bottom:2px solid var(--nav-rule);border-radius:2px}
.topnav a{position:absolute;top:14px;display:flex;align-items:center;gap:5px;
  color:#fff;font-weight:700;font-size:9.6px;text-decoration:none;height:18px}
.topnav svg{width:16px;height:16px}
.panel{position:absolute;left:109px;width:619px;background:var(--panel);
  border-radius:2px;box-shadow:0 2px 2px var(--panel-edge)}
.orb{position:absolute;left:16px;width:90px;height:90px;border-radius:50%;
  background:linear-gradient(var(--orb-light) 0%,#c3d8fb 45%,var(--orb-dark) 100%);
  box-shadow:0 3px 4px rgba(0,0,0,.12), inset 0 -6px 10px rgba(255,255,255,.35);
  display:flex;align-items:center;justify-content:center;text-align:center;
  font-weight:700;font-size:12px;line-height:15px;color:#444c5a;top:50%;margin-top:-45px}
.fields{position:absolute;display:grid;grid-template-columns:116px 1fr;grid-auto-rows:var(--row);align-items:center}
.fields dt{font-weight:700;color:var(--label)}
.fields dd{color:var(--value)}
.fields .multi{line-height:13.6px;align-self:start;padding-top:5px}
.col-left{left:148px}
.col-right{left:405px}
.site-footer{position:absolute;left:0;top:1123px;width:837px;height:77px;background:var(--footer)}
.social{position:absolute;left:0;right:0;top:23px;display:flex;justify-content:center;gap:10px;
  font-weight:700;font-size:10px;color:#222}
.copyright{position:absolute;left:0;right:0;top:50px;text-align:center;font-size:9.6px;color:#333}
.page-code{position:absolute;right:53px;top:50px;font-size:9.6px;color:#333}
</style>
</head>
<body>

<nav class="topnav">
  <a style="left:13px" href="#"><svg viewBox="0 0 16 16"><path d="M4 1h6l3 3v11H4z" fill="none" stroke="#fff" stroke-width="1.4"/><path d="M6 13h3M7.5 11.5v3" stroke="#fff" stroke-width="1.2"/></svg>Lead Category</a>
  <a style="left:128px" href="#"><svg viewBox="0 0 16 16"><rect x="1.5" y="3" width="11" height="11.5" fill="none" stroke="#fff" stroke-width="1.4"/><path d="M6 10l1-3 7-6 1.5 1.5-7 6z" fill="#fff"/></svg>Sticky Note</a>
  <a style="left:228px" href="#"><svg viewBox="0 0 16 16"><rect x="1" y="2.5" width="14" height="11" fill="none" stroke="#fff" stroke-width="1.4"/><path d="M1 5.5h14" stroke="#fff" stroke-width="1.4"/></svg>Snap Shot</a>
  <a style="left:327px" href="#"><svg viewBox="0 0 16 16"><circle cx="8" cy="8" r="7.5" fill="#fff"/><path d="M8 3.5v6" stroke="#8fb3f2" stroke-width="2"/><circle cx="8" cy="12" r="1.1" fill="#8fb3f2"/></svg>Alerts</a>
  <a style="left:404px" href="#"><svg viewBox="0 0 16 16"><path d="M5 1h7v11H5z M3 3h7v12H3z" fill="none" stroke="#fff" stroke-width="1.2"/><path d="M5 7h3M5 9h3M5 11h3" stroke="#fff"/></svg>Lead Notes</a>
  <a style="left:509px" href="#"><svg viewBox="0 0 16 16"><rect x="1.5" y="2.5" width="13" height="12.5" fill="none" stroke="#fff" stroke-width="1.3"/><path d="M1.5 5.5h13M4 1v3M12 1v3M4 8h2M7 8h2M10 8h2M4 10.5h2M7 10.5h2M10 10.5h2M4 13h2M7 13h2" stroke="#fff" stroke-width="1.2"/></svg>Calendar</a>
</nav>

<section class="panel" style="top:82px;height:132px">
  <div class="orb">Clients</div>
  <dl class="fields col-left" style="--row:25px;top:14px;left:150px">
    <dt>Borrower:</dt><dd>Daniel Varga</dd>
    <dt>Application:</dt><dd>Joint</dd>
    <dt>Lead Stat:</dt><dd>3</dd>
    <dt>Demo Stat:</dt><dd>4</dd>
  </dl>
  <dl class="fields col-right" style="--row:25px;top:8px">
    <dt>Co-Borrower:</dt><dd>Elena Varga</dd>
    <dt>Relationship:</dt><dd>Husband &amp; Wife</dd>
    <dt>Add borrowers</dt><dd>N/A</dd>
  </dl>
</section>

<section class="panel" style="top:218px;height:132px">
  <div class="orb">Existing<br>Loan</div>
  <dl class="fields col-left" style="--row:25px;top:16px">
    <dt>Current Amount:</dt><dd>$335,758</dd>
    <dt>Current Loan:</dt><dd>30 year fix – 5.5%</dd>
    <dt>Apprx. Last Refi:</dt><dd>4 years ago</dd>
    <dt>Add more Loans:</dt><dd>$59,000 - Heloc</dd>
  </dl>
  <dl class="fields col-right" style="--row:24.5px;top:16px">
    <dt>How many loans:</dt><dd>2 Pay off both? Yes</dd>
    <dt>Current P &amp; I:</dt><dd>$2,200</dd>
    <dt>Tax &amp; Insurance:</dt><dd>$450</dd>
    <dt>Total Payment:</dt><dd>$2,650</dd>
  </dl>
</section>

<section class="panel" style="top:357px;height:131px">
  <div class="orb">New<br>Loan</div>
  <dl class="fields col-left" style="--row:24.5px;top:29px">
    <dt>New Amount:</dt><dd>$336,000</dd>
    <dt>New Loan:</dt><dd>30 year fix - “select”</dd>
    <dt>Quoted Rate:</dt><dd>5%</dd>
  </dl>
  <dl class="fields col-right" style="--row:24.5px;top:29px">
    <dt>New Loan Purpose:</dt><dd>Rate &amp; Term</dd>
    <dt>Closing Costs:</dt><dd>$450</dd>
    <dt>Lender Credit:</dt><dd>$450</dd>
  </dl>
</section>

<section class="panel" style="top:494px;height:131px">
  <div class="orb">Contact</div>
  <dl class="fields col-left" style="--row:24px;top:20px">
    <dt>Main Phone:</dt><dd>111-111-1111</dd>
    <dt>Email:</dt><dd>Elena@postbox.net</dd>
    <dt>Address:</dt><dd class="multi">418 Harbor Lane<br>Alder Bay CA 90417</dd>
  </dl>
  <dl class="fields col-right" style="--row:24.5px;top:20px">
    <dt>Main Phone:</dt><dd>111-111-1111</dd>
    <dt>Email:</dt><dd>Elena@postbox.net</dd>
    <dt>Address:</dt><dd class="multi">418 Harbor Lane<br>Alder Bay CA 90417</dd>
  </dl>
</section>

<section class="panel" style="top:631px;height:131px">
  <div class="orb">Credit</div>
  <dl class="fields col-left" style="--row:21.2px;top:10px">
    <dt>DOB:</dt><dd>02/22/1975</dd>
    <dt>Daniel’s Social:</dt><dd>234-55-6477</dd>
    <dt>Credit Score:</dt><dd>700 688 744</dd>
    <dt>Credit Pull Date:</dt><dd>04/28/14</dd>
    <dt>DTI:</dt><dd>44% - 32%</dd>
  </dl>
  <dl class="fields col-right" style="--row:21.2px;top:11px">
    <dt>DOB:</dt><dd>01/25/1973</dd>
    <dt>Elena’s Social:</dt><dd>775-44-2222</dd>
    <dt>Credit Score:</dt><dd>712 694 708</dd>
    <dt>Credit Age:</dt><dd>2 Days</dd>
    <dt>Credit Impression:</dt><dd>Excellent</dd>
  </dl>
</section>

<section class="panel" style="top:768px;height:131px">
  <div class="orb">Property</div>
  <dl class="fields col-left" style="--row:20.5px;top:13px">
    <dt>Address:</dt><dd>418 Harbor Lane</dd>
    <dt></dt><dd>Alder Bay CA 90417</dd>
    <dt>Property Type:</dt><dd>SFR</dd>
    <dt>Residency:</dt><dd>Primary</dd>
    <dt>Year Built:</dt><dd>1981</dd>
  </dl>
  <dl class="fields col-right" style="--row:20.5px;top:11px">
    <dt>Subject Property:</dt><dd>Yes - 1 of 3</dd>
    <dt>Number of Properties:</dt><dd>3 - Add More</dd>
    <dt>Special Upgrades:</dt><dd>Added a room &amp; roof</dd>
    <dt>Approximate Value:</dt><dd>$445,000</dd>
    <dt>Appraised Value:</dt><dd>$405,000</dd>
  </dl>
</section>

<section class="panel" style="top:906px;height:196px">
  <div class="orb" style="top:51px;margin-top:0">Income</div>
  <dl class="fields col-left" style="--row:20px;top:17px">
    <dt>Income Source:</dt><dd>Northfield Labs</dd>
    <dt>Address:</dt><dd>123 Cedar way</dd>
    <dt>Work phone:</dt><dd>555-555-5555</dd>
    <dt>Position:</dt><dd>Admin</dd>
    <dt>Length:</dt><dd>2 years</dd>
    <dt>Term:</dt><dd>3 years</dd>
    <dt>Income:</dt><dd>$3,000</dd>
    <dt>Other income:</dt><dd>$ 1,500</dd>
  </dl>
  <dl class="fields col-right" style="--row:20px;top:17px">
    <dt>Income Source:</dt><dd>Northfield Labs</dd>
    <dt>Address:</dt><dd>123 Cedar way</dd>
    <dt>Work phone:</dt><dd>555-555-5555</dd>
    <dt>Position:</dt><dd>Manager</dd>
    <dt>Length:</dt><dd>2 years</dd>
    <dt>Term:</dt><dd>4 years</dd>
    <dt>Income:</dt><dd>$4,500</dd>
    <dt>Other income:</dt><dd>$ 1,950</dd>
  </dl>
</section>

<footer class="site-footer">
  <div class="social"><span>Feed</span><span>Page</span><span>Posts</span><span>Network</span></div>
  <p class="copyright">© Company Name ,All Rights Reserved</p>
  <span class="page-code">C5</span>
</footer>

</body>
</html>
```